Window company.

Hello,

We are a small family business located in Madrid, Spain that works nationwide to fix, change or mount the windows of your home / premises.

The group of possible clients to whom the flyer is focused ranges from 30 to 65 years, families in general who want comfort at home and extra savings every year in heating.

It must include not only graphics and a striking aesthetic in accordance with the concepts of wanting to reach / transmit the final product to the customer to sell the product.

Details to also include:

-Brief history of the company and its foundation in 2006. It will be subsequently translated into Spanish so put in words what you consider necessary so that the client stays with the concept that we are professionals.

--Specialized in exterior aluminum and PVC carpentry.

-We move to your home for a first visit and we provide the budget totally free without any commitment.

- Also payment facilities; up to 3 times, without interest.

-Contact details of the company. (WhatsApp, email, phone and location)
Open: Mon - Friday 11,00am - 9pm
Saturday: 12,00am - 7pm
Sunday: Closed

Also as a suggestion, to decide on your own, graphics of types of window openings, if you consider that anything that is striking for the client so it wonr be yet another advertising flyer.

We are open to all kinds of ideas, all of them involving marketing branding.

We are open to any type of idea and we want to stand out, the construction world is tough and we have an idea to grow, taking into account that it must not only be beautiful but commercial to attract potential customers with all kinds of purchasing power.

Thank you.

```html
<!DOCTYPE html>
<html lang="en">
<head>
<meta charset="utf-8">
<title>Ventara Windows Flyer</title>
<link href="https://fonts.googleapis.com/css2?family=Oswald:wght@400;500&family=Source+Sans+3:wght@400;600;700&display=swap" rel="stylesheet">
<style>
  :root{
    --red:#c8292b;
    --dark:#2e2e2e;
    --grey:#8f8f8f;
    --band:#9a9a9a;
    --light:#f2f2f2;
    --white:#ffffff;
    --stage:#e6e6e6;
  }
  *{margin:0;padding:0;box-sizing:border-box}
  html,body{width:1200px;height:800px;overflow:hidden;background:var(--stage)}
  .canvas{position:relative;width:1200px;height:800px}
  .flyer{position:absolute;left:326px;top:11px;width:595px;height:845px;background:var(--white);
    transform:scale(.92);transform-origin:0 0;overflow:hidden;font-family:"Source Sans 3",sans-serif;color:var(--dark);
    box-shadow:0 4px 18px rgba(0,0,0,.18)}
  .abs{position:absolute}
  .brand{left:112px;top:58px;font-size:27px;font-weight:600;letter-spacing:1px;color:var(--grey)}
  .social{top:27px;width:26px;height:26px;border:1.5px solid #aaa;border-radius:50%}
  .hero-bg{left:0;top:120px;width:595px;height:250px;background:linear-gradient(90deg,#f6f6f6,#eaeaea)}
  .hero-photo{left:0;top:70px;width:595px;height:298px;
    background:linear-gradient(120deg,#e9d6bf 0%,#d9b994 35%,#cfe6ee 60%,#e2cdb2 100%);
    clip-path:polygon(300px 0,595px 0,595px 298px,230px 298px,250px 50px)}
  .frame-line{left:0;top:0}
  .headline{left:24px;top:136px;font-family:"Oswald",sans-serif;font-weight:500;font-size:33px;line-height:36px;color:var(--dark);letter-spacing:.5px}
  .offer-band{left:0;top:252px;width:296px;height:42px;background:var(--red);
    clip-path:polygon(0 0,282px 0,296px 42px,0 42px)}
  .offer-text{left:23px;top:256px;font-family:"Oswald",sans-serif;font-size:22px;color:var(--white);letter-spacing:-.3px}
  .quality{left:25px;top:302px;font-family:"Oswald",sans-serif;font-weight:500;font-size:20px;color:var(--dark);letter-spacing:-.3px}
  .about{left:0;top:368px;width:595px;height:168px;background:linear-gradient(180deg,#fff,#eeeeee)}
  .about-title{left:24px;top:389px;font-size:16px;font-weight:700;color:var(--red)}
  .about-body{left:24px;top:418px;width:255px;font-size:12.5px;line-height:16px;text-align:justify}
  .divider{left:296px;top:385px;width:1px;height:118px;background:#bbb}
  .spec-title{left:311px;top:391px;width:270px;font-size:11.5px;font-weight:700;line-height:14px;text-transform:uppercase}
  .spec-body{left:312px;top:428px;width:275px;font-size:12px;line-height:16px;letter-spacing:-.3px}
  .pay-btn{left:313px;top:469px;width:272px;height:24px;background:var(--red);color:var(--white);font-size:10.5px;font-weight:700;
    display:flex;align-items:center;justify-content:center;letter-spacing:-.2px}
  .services-tab{left:0;top:518px;width:196px;height:28px;background:var(--red);clip-path:polygon(0 0,196px 0,184px 28px,0 28px)}
  .services-title{left:24px;top:520px;font-size:16px;font-weight:700;color:var(--white)}
  .services{left:0;top:535px;width:595px;height:171px;background:linear-gradient(90deg,#a3a3a3,#8c8c8c 60%,#a0a0a0);
    border-top:2px solid var(--red);border-bottom:2px solid var(--red)}
  .service{display:flex;align-items:center;gap:13px;color:var(--white);font-size:14.5px;font-weight:600;text-transform:uppercase;letter-spacing:-.3px}
  .service svg{width:32px;height:32px;flex:none}
  .hours{left:0;top:730px;width:595px;text-align:center;font-size:12.5px}
  .footer{left:0;top:783px;width:595px;height:62px;background:var(--band)}
  .call{left:55px;top:768px;width:478px;height:29px;border-radius:15px;background:var(--red);color:var(--white);
    display:flex;align-items:center;justify-content:center;gap:5px;font-size:13.5px;font-weight:700}
  .call .num{font-size:15px}
  .contact{left:0;top:803px;width:595px;text-align:center;color:var(--white);font-size:13px;line-height:17px}
</style>
</head>
<body>
<div class="canvas">
  <article class="flyer">
    <div class="abs hero-bg"></div>
    <div class="abs hero-photo" role="img" aria-label="Photo of a smiling family at home holding a roof shape over their heads"></div>
    <svg class="abs frame-line" width="595" height="130" viewBox="0 0 595 130">
      <polyline points="0,120 258,120 300,70 595,70" fill="none" stroke="var(--red)" stroke-width="3"/>
    </svg>

    <div class="abs brand">VENTARA</div>
    <div class="abs social" style="left:416px"></div>
    <div class="abs social" style="left:459px"></div>
    <div class="abs social" style="left:503px"></div>
    <div class="abs social" style="left:547px"></div>

    <h1 class="abs headline">SAVINGS<br>EVERY YEAR<br>IN HEATING</h1>
    <div class="abs offer-band"></div>
    <p class="abs offer-text">Budgets with no obligation.</p>
    <p class="abs quality">QUALITY GUARANTEED!</p>

    <section class="abs about"></section>
    <h2 class="abs about-title">WHO WE ARE</h2>
    <p class="abs about-body">We are a small family business located in Madrid, Spain that works nationwide to fix, change or mount the windows of your home / premises founded 2006.</p>
    <div class="abs divider"></div>
    <h3 class="abs spec-title">Specialized in exterior aluminum and PVC carpentry.</h3>
    <p class="abs spec-body">We move to your home for a first visit and we provide the budget totally free without any commitment.</p>
    <div class="abs pay-btn">PAYMENT FACILITIES; UP TO 3 TIMES, WITHOUT INTEREST</div>

    <section class="abs services" role="img" aria-label="Faded photo of a suburban house behind the service list"></section>
    <div class="abs services-tab"></div>
    <h2 class="abs services-title">OUR SERVICES</h2>

    <div class="abs service" style="left:30px;top:551px"><svg viewBox="0 0 32 32"><rect x="1" y="1" width="30" height="30" rx="3" fill="none" stroke="#ddd" stroke-width="1.5"/><rect x="7" y="7" width="18" height="18" fill="var(--red)"/><path d="M10 17 16 11 22 17M12 16v6h8v-6" stroke="#fff" stroke-width="1.5" fill="none"/></svg>Outdoor carpentry</div>
    <div class="abs service" style="left:30px;top:587px"><svg viewBox="0 0 32 32"><rect x="1" y="1" width="30" height="30" rx="3" fill="none" stroke="#ddd" stroke-width="1.5"/><rect x="7" y="7" width="18" height="18" fill="var(--red)"/><path d="M7 13h18M10 16h12v7H10z" stroke="#fff" stroke-width="1.5" fill="none"/></svg>Toldos</div>
    <div class="abs service" style="left:30px;top:623px"><svg viewBox="0 0 32 32"><rect x="1" y="1" width="30" height="30" rx="3" fill="none" stroke="#ddd" stroke-width="1.5"/><rect x="7" y="7" width="18" height="18" fill="var(--red)"/><path d="M10 10h12v12H10zM16 10v12" stroke="#fff" stroke-width="1.5" fill="none"/></svg>Aluminum</div>
    <div class="abs service" style="left:30px;top:659px"><svg viewBox="0 0 32 32"><rect x="1" y="1" width="30" height="30" rx="3" fill="none" stroke="#ddd" stroke-width="1.5"/><rect x="7" y="7" width="18" height="18" fill="var(--red)"/><path d="M10 10h12v12H10zM16 10v12M10 16h12" stroke="#fff" stroke-width="1.5" fill="none"/></svg>Glazing</div>

    <div class="abs service" style="left:299px;top:551px"><svg viewBox="0 0 32 32"><rect x="1" y="1" width="30" height="30" rx="3" fill="none" stroke="#ddd" stroke-width="1.5"/><rect x="7" y="7" width="18" height="18" fill="var(--red)"/><path d="M10 10h12v12H10zM16 10v12M10 16h12" stroke="#fff" stroke-width="1.5" fill="none"/></svg>PVC</div>
    <div class="abs service" style="left:299px;top:587px"><svg viewBox="0 0 32 32"><rect x="1" y="1" width="30" height="30" rx="3" fill="none" stroke="#ddd" stroke-width="1.5"/><rect x="7" y="7" width="18" height="18" fill="var(--red)"/><path d="M10 12h12M10 16h12M10 20h12M12 10v12M16 10v12M20 10v12" stroke="#fff" stroke-width=".8" fill="none"/></svg>Mosquito nets</div>
    <div class="abs service" style="left:299px;top:623px"><svg viewBox="0 0 32 32"><rect x="1" y="1" width="30" height="30" rx="3" fill="none" stroke="#ddd" stroke-width="1.5"/><path d="M8 10 20 7 25 22 12 25z" fill="var(--red)"/><path d="M11 13 19 11 22 20 14 22z" stroke="#fff" stroke-width="1.2" fill="none"/></svg>Lucernarios</div>
    <div class="abs service" style="left:299px;top:659px"><svg viewBox="0 0 32 32"><rect x="1" y="1" width="30" height="30" rx="3" fill="#fff" stroke="#ddd" stroke-width="1.5"/><path d="M16 9v14M9 16h14" stroke="var(--red)" stroke-width="2"/></svg>And much more</div>

    <p class="abs hours">OPEN: MON - FRIDAY 11,00AM - 9PM &nbsp;|&nbsp; SATURDAY: 12,00AM - 7PM &nbsp;|&nbsp; SUNDAY: CLOSED</p>

    <div class="abs footer"></div>
    <div class="abs call">Call Ventara on
      <svg width="13" height="13" viewBox="0 0 16 16"><circle cx="8" cy="8" r="6.8" fill="none" stroke="#fff" stroke-width="1.3"/><path d="M5.5 4.5c-.6.6-.5 1.8.6 3.3 1.2 1.6 2.6 2.5 3.4 2.3l.8-.9-1.3-1-.7.5c-.6-.3-1.3-1.1-1.6-1.7l.5-.7-1-1.3z" fill="#fff"/></svg>
      <span class="num">+34 600 12 34 56</span> for more information</div>
    <p class="abs contact">hello@ventarawindows.com | www.ventarawindows.com<br>Calle del Ejemplo 12, Polígono Norte, Madrid, Spain 28001</p>
  </article>
</div>
</body>
</html>
```